B2B EDM Banner Design- Specialist Tech Company

We need a new top-of-email banner for our EDM campaigns for Varnel Brix (www.varnelbrix-example.com
). This banner will sit at the top of every email and must immediately signal the brand, look modern and professional, and be visually aligned with the tech/IT audience.
Size of the banner: Around 728x90 - it must fit at the top of an email blast.
Purpose of the Banner
Establish a strong, recognizable brand identity across all Varnel Brix EDMs
visually consistent with existing banners created for other brands (see reference examples provided)
Communicate Varnel Brix’s value proposition at a glance
Brand Name
Varnel Brix
Tagline (must appear in the banner)
“11,322 whitepapers from 726 companies”
Design Requirements
Style & Tone
Modern, clean, and professional
Tech-centric look and feel
High-quality, sleek, and corporate
Eye-catching but not cluttered
Should feel premium and authoritative
Layout & Composition
Full-width banner for email header
Horizontal orientation similar to the Plomtar and Quindle Staff Archive examples
Include space for the brand name/logo prominently on the left or centered
Integrate the tagline in a readable, secondary position
Optional: a subtle background texture or tech-related abstract pattern (circuitry, network nodes, gradient, etc.)
No busy imagery—should feel clean and trustworthy
Color Palette
Use colors consistent with Varnel Brix branding from www.varnelbrix-example.com
Blues, greys, blacks, and tech-style gradients preferred
Should feel consistent with a B2B IT audience
Typography
Clean, sans-serif fonts (professional/tech-aligned)
Brand name should be bold and prominent
Tagline should be smaller, but still readable on desktop and mobile
Imagery (if used)
Abstract tech shapes, network visuals, geometric patterns, or gradient overlays
Avoid photography of people
Keep imagery subtle so text remains legible
Call-to-Action Button (optional)
None required in this banner (unlike the HR examples)
Banner should remain a pure brand header
Deliverables
Final banner in PNG and JPG formats
2–3 design variations (if possible) for A/B testing
Dimensions optimized for EDM: ~600–700px wide (standard email width), proportionate height

```html
<!DOCTYPE html>
<html lang="en">
<head>
<meta charset="UTF-8">
<title>Varnel Brix – EDM Header Banner</title>
<link href="https://fonts.googleapis.com/css2?family=Montserrat:wght@300;400;700;800&display=swap" rel="stylesheet">
<style>
  :root {
    --backdrop: #c4c4c4;
    --navy: #002a54;
    --navy-deep: #00152e;
    --night: #011a3a;
    --sky: #009fe0;
    --white: #ffffff;
    --ink: #1c1c1c;
  }
  * { margin: 0; padding: 0; box-sizing: border-box; }
  html, body {
    width: 1200px;
    height: 930px;
    overflow: hidden;
    background: var(--backdrop);
  }
  .banner {
    position: absolute;
    left: 52px;
    top: 381px;
    width: 1096px;
    height: 135px;
    background: var(--white);
    overflow: hidden;
    font-family: "Montserrat", sans-serif;
  }
  .banner-shapes {
    position: absolute;
    inset: 0;
    width: 100%;
    height: 100%;
  }
  .tagline {
    position: absolute;
    left: 27px;
    top: 24px;
    color: var(--white);
    font-weight: 300;
    font-size: 43px;
    line-height: 45px;
    letter-spacing: 0.6px;
    white-space: nowrap;
  }
  .tagline .figure {
    color: var(--sky);
    font-weight: 700;
    letter-spacing: -0.5px;
  }
  .brand-dot {
    position: absolute;
    left: 598px;
    top: 18px;
    width: 98px;
    height: 98px;
    border-radius: 50%;
    background: var(--sky);
  }
  .brand {
    position: absolute;
    left: 722px;
    top: 22px;
    width: 360px;
    text-align: center;
  }
  .brand-name {
    color: var(--navy);
    font-weight: 800;
    font-size: 47px;
    line-height: 50px;
    letter-spacing: -0.3px;
    white-space: nowrap;
  }
  .brand-rule {
    height: 1.5px;
    background: var(--sky);
    margin-top: 2px;
  }
  .brand-claim {
    margin-top: 5px;
    color: var(--navy);
    font-weight: 800;
    font-size: 14px;
    letter-spacing: 9.4px;
    margin-right: -9.4px;
    white-space: nowrap;
  }
  .brand-web {
    margin-top: 10px;
    color: var(--ink);
    font-weight: 400;
    font-size: 11px;
    letter-spacing: 4.2px;
    white-space: nowrap;
  }
</style>
</head>
<body>
  <div class="banner">
    <svg class="banner-shapes" viewBox="0 0 1096 135" preserveAspectRatio="none">
      <defs>
        <linearGradient id="nightGlow" x1="0" y1="0" x2="1" y2="0.4">
          <stop offset="0" stop-color="#0a3f86"/>
          <stop offset="0.35" stop-color="#021f4a"/>
          <stop offset="0.75" stop-color="#01193a"/>
          <stop offset="1" stop-color="#000c1e"/>
        </linearGradient>
      </defs>
      <path d="M500 0 C590 25 625 95 553 135 L605 135 C640 80 610 20 503 0 Z" fill="var(--sky)"/>
      <path d="M0 0 H497 C566 30 575 95 508 135 H0 Z"
            fill="url(#nightGlow)" stroke="var(--white)" stroke-width="2.5"
            role="img" aria-label="Dark blue abstract tech backdrop with soft glowing light points"/>
    </svg>

    <p class="tagline">
      <span class="figure">11,322</span> WHITEPAPERS<br>
      FROM <span class="figure">726</span> COMPANIES
    </p>

    <div class="brand-dot"></div>
    <div class="brand">
      <div class="brand-name">VARNEL BRIX</div>
      <div class="brand-rule"></div>
      <div class="brand-claim">FOR IT PROFESSIONALS</div>
      <div class="brand-web">WWW.VARNELBRIX-EXAMPLE.COM</div>
    </div>
  </div>
</body>
</html>
```